A first time author needs a book cover design to tell his story about a captivating spiritual conver

“ Where the lantern waits “ Is about a man raised in the violent streets of Boston’s Charlestown. His parents gave him the gift of faith. At the age of 20 an argument with his dad ends in a heart attack death. He goes on to lead a very successful financial life filled with vices that could destroy him or his family at any time. Then 35 years after this tragic death, he is invited to Bosnia Medjugorje, and has a life changing conversion. The book is a collection of stories and experiences that will inspire change in one's own pilgrimage of life. An effective design should be one the draws the reader to this story, and show this book can change your heart.

Target Market(s)

Adult male & female within USA and English speaking countries. Christian bookstores and retreat centers.

Industry/Entity Type

Financial

Font styles to use
Sans Serif

Requirements
Must have
• • Communicate clear and quickly to reader
• Lead your audience to the title
• Have a relevant visual theme or concept to attract reader
• Clear and simple not confusing
• Good use of color that attracts and is consistent with your theme
• Word are visible and have a dramatic affect
• Cover has a focal point
• Must stand out at K & T, Parcelo

```html
<!DOCTYPE html>
<html lang="en">
<head>
<meta charset="utf-8">
<title>Where the lantern waits — cover</title>
<link rel="stylesheet" href="https://fonts.googleapis.com/css2?family=Work+Sans:wght@400;500&display=swap">
<style>
  :root {
    --page-bg: #efefed;
    --forest-deep: #1c3326;
    --forest-dark: #2c4a38;
    --forest-mid: #5b7663;
    --mist-light: #c4caa6;
    --mist-pale: #e0e1c6;
    --title-ink: #ffffff;
    --byline-ink: #f1f1e8;
  }
  * { margin: 0; padding: 0; box-sizing: border-box; }
  html, body {
    width: 1200px;
    height: 900px;
    overflow: hidden;
    background: var(--page-bg);
  }
  .canvas {
    width: 1200px;
    height: 900px;
    display: flex;
    align-items: center;
    justify-content: center;
  }
  .cover {
    position: relative;
    width: 560px;
    height: 800px;
    overflow: hidden;
    box-shadow: 0 12px 32px rgba(0, 0, 0, 0.2);
    background: var(--forest-deep);
  }
  .cover-photo {
    position: absolute;
    inset: 0;
    background:
      radial-gradient(ellipse 55% 45% at 52% 38%, var(--mist-pale) 0%, rgba(224, 225, 198, 0.55) 45%, rgba(224, 225, 198, 0) 100%),
      linear-gradient(90deg, var(--forest-dark) 0%, var(--forest-mid) 22%, var(--mist-light) 50%, var(--forest-mid) 78%, var(--forest-dark) 100%);
  }
  .cover-shade {
    position: absolute;
    inset: 0;
    background: linear-gradient(180deg, rgba(28, 51, 38, 0.55) 0%, rgba(28, 51, 38, 0) 22%, rgba(28, 51, 38, 0) 55%, rgba(28, 51, 38, 0.85) 100%);
  }
  .title {
    position: absolute;
    left: 44px;
    top: 250px;
    font-family: "Work Sans", sans-serif;
    font-weight: 500;
    font-size: 92px;
    line-height: 0.9;
    letter-spacing: -2px;
    color: var(--title-ink);
    text-shadow: 0 3px 10px rgba(0, 0, 0, 0.35);
  }
  .title span { display: block; }
  .title .line-2 { padding-left: 40px; }
  .title .line-3 { padding-left: 40px; }
  .title .line-4 { padding-left: 120px; }
  .byline {
    position: absolute;
    right: 34px;
    bottom: 70px;
    font-family: "Work Sans", sans-serif;
    font-weight: 400;
    font-size: 19px;
    color: var(--byline-ink);
    letter-spacing: 0.3px;
  }
  .byline .divider { margin: 0 10px; }
</style>
</head>
<body>
  <main class="canvas">
    <section class="cover">
      <div class="cover-photo" role="img" aria-label="Photograph of a misty forest with tall dark tree trunks rising into pale green fog"></div>
      <div class="cover-shade"></div>
      <h1 class="title">
        <span class="line-1">Where</span>
        <span class="line-2">the</span>
        <span class="line-3">lantern</span>
        <span class="line-4">waits</span>
      </h1>
      <p class="byline">Aaron Whitcombe<span class="divider">|</span>Lucia Marenco</p>
    </section>
  </main>
</body>
</html>
```